Construction proffessionals servicing the inner suburbs of Melbournes NorthWest specialising in aler

I would like a web site that is sharp, contemporary and simple to navigate, ie.not too many pages. i would like a home page with some info about us, who we are what our history is and my passion for building and construction based on impeccable customer focus. i would like a projects page and somewhere for clients to add testimonials. i would like a project calculator as well so prospective clients can work out a rough budget prior to contacting. i would like the colours to be in line with my logo which i have uploaded. i have many photos which can be used and can be shared via drop box when required. I would like it to be personal to capture our transparent process. i would like to add our company process as well. be brave and take risks.

Target Market(s)

People renovating and extending their homes, people needing inspections on new homes and pre-purchase inspections

Industry/Entity Type

Construction

Number of Pages Required

5+ page

Requirements
Must have
• Professional, easy to navigate, provide viewers with a happy experience, look great, contacts, project calculator, link through to my training company www.ktrp.vic.edu.au also check ormwaybuilds on instagram for pics
Nice to have
• Links to instagram, fonts to match email signature

```html
<!DOCTYPE html>
<html lang="en">
<head>
<meta charset="utf-8">
<title>Ormway Builds — Home</title>
<link href="https://fonts.googleapis.com/css2?family=Open+Sans:wght@400;600;700;800&display=swap" rel="stylesheet">
<style>
:root{
  --orange:#f7941d;
  --orange-dark:#e07d0a;
  --ink:#333;
  --muted:#777;
  --dark:#3a3a3a;
  --footer:#2b2b2b;
  --footer-bottom:#1f1f1f;
  --line:#e2e2e2;
  --bg:#fff;
}
*{box-sizing:border-box;margin:0;padding:0}
html,body{width:855px;height:1200px;overflow:hidden;background:var(--bg)}
body{font-family:"Open Sans",Arial,sans-serif;color:var(--ink);position:relative;font-size:8px;line-height:1.45}
.abs{position:absolute}

/* header */
.site-header{left:0;top:0;width:855px;height:46px;background:#fff;border-bottom:1px solid var(--line)}
.brand{left:70px;top:8px;height:30px;display:flex;align-items:center;gap:6px;font-weight:800;font-size:15px;color:var(--orange)}
.brand-mark{width:22px;height:22px;background:var(--orange)}
.main-nav{left:420px;top:0;height:46px;display:flex;align-items:center;gap:30px;font-size:9px;color:#555}
.main-nav .active{color:var(--orange);font-weight:700}
.nav-cta{left:718px;top:13px;width:97px;height:20px;background:var(--orange);color:#fff;font-size:8px;font-weight:700;text-align:center;line-height:20px}

/* hero */
.hero{left:0;top:46px;width:855px;height:285px;background:linear-gradient(180deg,#b9a48e 0%,#8a8078 35%,#5f5f66 60%,#3b3b42 100%)}
.hero-title{left:70px;top:262px;color:#fff;font-weight:800;font-size:17px;line-height:1.2;letter-spacing:.3px;text-shadow:0 1px 3px rgba(0,0,0,.5)}

/* welcome */
.welcome{left:70px;top:348px;width:200px}
.welcome h2{font-size:11px;font-weight:800;line-height:1.25;color:#222}
.welcome .rule{width:34px;height:2px;background:var(--orange);margin:6px 0 8px}
.welcome p{color:var(--muted);font-size:7.5px}
.contact-list{list-style:none;margin-top:10px;font-size:7.5px}
.contact-list li{display:flex;align-items:center;gap:5px;margin-bottom:4px;color:#555}
.contact-list b{color:var(--ink)}
.contact-list .ic{width:6px;height:6px;border-radius:50%;background:var(--orange)}

/* calculator */
.calculator{left:285px;top:345px;width:300px;height:255px;background:var(--orange);padding:14px 14px}
.calculator h3{color:#fff;font-size:10px;font-weight:800}
.calculator .rule{width:30px;height:2px;background:#fff;margin:5px 0 10px}
.calc-grid{display:grid;grid-template-columns:1fr 1fr;gap:8px 10px}
.select{height:17px;background:#fff;border:1px solid #e9a54f;font-size:6.5px;color:#999;padding:0 6px;line-height:15px;position:relative}
.select:after{content:"";position:absolute;right:6px;top:6px;border:3px solid transparent;border-top-color:#888}
.calc-actions{display:flex;align-items:center;gap:12px;margin-top:14px}
.btn-submit{background:#c0392b;color:#fff;font-weight:700;font-size:7.5px;padding:5px 14px}
.calc-actions span{color:#fff;font-size:7px}
.estimate{margin-top:14px;border-top:1px solid rgba(255,255,255,.45);padding-top:10px;color:#fff;font-size:7.5px;display:flex;align-items:baseline;gap:8px}
.estimate strong{font-size:16px;font-weight:800}

/* stories */
.stories-photo{left:600px;top:345px;width:215px;height:105px;background:linear-gradient(160deg,#f1f1f1,#d9c29a 60%,#c9a469)}
.stories{left:600px;top:458px;width:215px}
.stories h4{font-size:9px;font-weight:800}
.stories p{color:var(--muted);font-size:7px;margin:4px 0 7px}
.btn-small{display:inline-block;background:#c0392b;color:#fff;font-size:6.5px;font-weight:700;padding:3px 9px}

/* help boxes */
.help-row{left:70px;top:612px;width:515px;display:flex;gap:8px}
.help-box{flex:1;height:48px;background:var(--dark);color:#fff;display:flex;align-items:center;gap:8px;padding:0 10px;font-weight:800;font-size:8.5px;line-height:1.15}
.help-box .ic{width:22px;height:22px;border-radius:50%;border:2px solid var(--orange);flex:none;display:flex;align-items:center;justify-content:center}
.help-box.first{background:#c0392b}
.help-box.first .ic{border-color:#fff}

/* clients */
.clients{left:600px;top:590px;width:215px;height:285px;border:1px solid var(--line);padding:14px;text-align:center}
.clients h4{font-size:9px;font-weight:800;text-align:left}
.avatar{width:64px;height:64px;border-radius:50%;margin:12px auto 8px;background:linear-gradient(180deg,#d8d8d8,#9aa3ad)}
.clients .name{color:var(--orange);font-weight:700;font-size:8.5px}
.clients .role{color:var(--muted);font-size:6.5px;margin-bottom:6px}
.clients p{color:var(--muted);font-size:7px;text-align:left}

/* projects */
.tabs{left:70px;top:682px;width:515px;display:flex;border-bottom:2px solid var(--orange)}
.tab{font-size:7.5px;padding:5px 14px;background:#f1f1f1;color:#666;margin-right:2px}
.tab.active{background:var(--orange);color:#fff;font-weight:700}
.project-grid{left:70px;top:712px;width:515px;display:grid;grid-template-columns:repeat(4,1fr);gap:10px}
.project-photo{height:75px}
.p1{background:linear-gradient(180deg,#9cc2e0,#b08a64)}
.p2{background:linear-gradient(180deg,#a9c7de,#7c6a57)}
.p3{background:linear-gradient(180deg,#c9d9e6,#a5783f)}
.p4{background:linear-gradient(180deg,#b7c7d3,#8d8d8d)}
.project h5{color:var(--orange);font-size:7px;font-weight:700;margin-top:5px}
.project .meta{font-size:6.5px;color:#555;margin-top:3px}
.project .meta i{display:inline-block;width:5px;height:5px;background:var(--orange);border-radius:50%;margin-right:3px}

/* footer */
.site-footer{left:0;top:892px;width:855px;height:275px;background:var(--footer);color:#aaa}
.f-col{position:absolute;top:22px}
.f-col h6{color:#fff;font-size:8.5px;font-weight:800;margin-bottom:10px}
.f-col p{font-size:7px;margin-bottom:7px}
.f-col .date{color:var(--orange)}
.f-col ul{list-style:none;font-size:7px}
.f-col li{margin-bottom:6px}
.social li{display:flex;align-items:center;gap:7px;margin-bottom:9px}
.social .dot{width:16px;height:16px;border-radius:50%;background:#444;border:1px solid #555}
.footer-bottom{left:0;top:1167px;width:855px;height:33px;background:var(--footer-bottom);color:#888;font-size:7px;text-align:center;line-height:33px}
</style>
</head>
<body>

<header class="site-header abs">
  <div class="brand abs"><span class="brand-mark"></span>Ormway</div>
  <nav class="main-nav abs">
    <span class="active">Home</span><span>About us</span><span>Projects</span><span>Testimonials</span><span>Contact us</span>
  </nav>
  <div class="nav-cta abs">BOOKING LEAD</div>
</header>

<section class="hero abs" role="img" aria-label="City skyline photograph of Melbourne high-rises at dusk"></section>
<h1 class="hero-title abs">PROVIDING QUALITY EXPERT ADVICE,<br>COMMON SENSE AND FRIENDLY PROFESSIONAL SERVICE</h1>

<section class="welcome abs">
  <h2>WELCOME TO THE<br>ORMWAY BUILDS PTY LTD WEBSITE</h2>
  <div class="rule"></div>
  <p>If you renovate or extend your home, we are here to help. Our team has built and inspected homes across the inner north west for many years, with a clear and open process from first visit to handover. We care about every client and every detail of the job.</p>
  <ul class="contact-list">
    <li><span class="ic"></span><b>Office:</b> (03) 9410 2276</li>
    <li><span class="ic"></span><b>Mobile:</b> 0412 555 018</li>
    <li><span class="ic"></span><b>Email:</b> info@ormwaybuilds.com.au</li>
  </ul>
</section>

<section class="calculator abs">
  <h3>PROJECT CALCULATOR</h3>
  <div class="rule"></div>
  <div class="calc-grid">
    <div class="select">Select City</div><div class="select">Select Project</div>
    <div class="select">Select Type</div><div class="select">Select Area</div>
    <div class="select">Select Size</div><div class="select">Select Unit</div>
  </div>
  <div class="calc-actions"><span class="btn-submit">SUBMIT NOW</span><span>Clear all</span></div>
  <div class="estimate">Your estimation amount is <strong>$20, 000 000</strong></div>
</section>

<div class="stories-photo abs" role="img" aria-label="Photo of builders in hard hats on a site"></div>
<section class="stories abs">
  <h4>TOP STORIES</h4>
  <p>A short look at our latest builds, the people behind them and the care we put into each home we work on.</p>
  <span class="btn-small">READ MORE</span>
</section>

<div class="help-row abs">
  <div class="help-box first"><span class="ic">
    <svg width="10" height="10" viewBox="0 0 10 10"><path d="M2 1l2 2-1 1.5c.6 1.2 1.3 1.9 2.5 2.5L7 6l2 2-1.5 1.5C4 9 1 6 .5 2.5z" fill="#fff"/></svg>
  </span>HOW CAN<br>WE HELP YOU?</div>
  <div class="help-box"><span class="ic">
    <svg width="10" height="10" viewBox="0 0 10 10"><path d="M5 1L1 9h8z" fill="none" stroke="#f7941d" stroke-width="1.2"/></svg>
  </span>DO YOU HAVE A<br>BUILDING ISSUE?</div>
  <div class="help-box"><span class="ic">
    <svg width="10" height="10" viewBox="0 0 10 10"><path d="M1.5 5.5l2.2 2.2L8.5 2.5" fill="none" stroke="#f7941d" stroke-width="1.4"/></svg>
  </span>DO YOU NEED<br>BUILDING ADVICE</div>
</div>

<aside class="clients abs">
  <h4>CLIENTS SAYS</h4>
  <div class="avatar" role="img" aria-label="Portrait photo of a client"></div>
  <div class="name">Marcus Hale</div>
  <div class="role">Renovation Client</div>
  <p>The team kept us in the loop at every stage of our extension. Clear costs, tidy site and a finish we are proud of. We would not build with anyone else and will be back for our next home project.</p>
</aside>

<div class="tabs abs">
  <span class="tab active">Recent Projects</span><span class="tab">Upcoming Projects</span><span class="tab">Government Projects</span>
</div>
<div class="project-grid abs">
  <article class="project"><div class="project-photo p1" role="img" aria-label="Photo of a renovated brick home"></div><h5>Home extension in Brunswick</h5><div class="meta"><i></i>Date: 12 Mar 2015</div></article>
  <article class="project"><div class="project-photo p2" role="img" aria-label="Photo of a house under construction"></div><h5>New build in Coburg North</h5><div class="meta"><i></i>Date: 04 Feb 2015</div></article>
  <article class="project"><div class="project-photo p3" role="img" aria-label="Photo of a timber frame home"></div><h5>Second storey in Essendon</h5><div class="meta"><i></i>Date: 21 Jan 2015</div></article>
  <article class="project"><div class="project-photo p4" role="img" aria-label="Photo of a modern townhouse front"></div><h5>Townhouse in Moonee Ponds</h5><div class="meta"><i></i>Date: 09 Dec 2014</div></article>
</div>

<footer class="site-footer abs">
  <div class="f-col" style="left:70px;width:200px">
    <h6>LATEST NEWS</h6>
    <p>Simple steps to plan your next home renovation on time and on budget.</p>
    <p class="date">Posted on 12 March 2015</p>
    <p>Why a pre-purchase inspection can save you money before you sign a contract.</p>
  </div>
  <div class="f-col" style="left:315px">
    <h6>WELCOME</h6>
    <ul><li>Home</li><li>About us</li><li>Projects</li><li>Testimonials</li><li>Contact us</li></ul>
  </div>
  <div class="f-col" style="left:510px">
    <h6>INFORMATION</h6>
    <ul><li>Privacy Policy</li><li>Terms &amp; Conditions</li><li>Site Map</li></ul>
  </div>
  <div class="f-col social" style="left:700px">
    <h6>FOLLOW US</h6>
    <ul><li><span class="dot"></span>Friends Page</li><li><span class="dot"></span>News Feed</li><li><span class="dot"></span>Work Profile</li><li><span class="dot"></span>Photo Stream</li></ul>
  </div>
</footer>
<div class="footer-bottom abs">© 2015 Ormway Builds. All Rights Reserved.</div>

</body>
</html>
```